International Marketing Company - Web Design Project

kVesta is a well-funded start up in London developing an Online Marketing Platform for small businesses in Europe.

We require a large number of high quality business web designs for our business website builder. Our business websites are completely integrated into our Online Marketing systems and therefore it is important for designers to comply with our Design Guidelines.

This initial contest is a trial for us to open up the design process to top designers for the Builders vertical (e.g. Builders, Electricians, Plumbers, Flooring, etc.). We have implemented a base html structure and design and included them in the files.

Use your creativity to design new and fresh designs based on the included elements (e.g. testimonials, business description, etc).

We will award the stated prize money for the top three designs.

Any designers that submit designs we feel are of a high enough quality but do not make the top 3 could still be compensated and WILL be invited to participate in our next vertical competition.

Therefore, we encourage designers to submit as many designs as possible as we may award up to 25 designs.

Submissions will be reviewed daily and feedback provided where possible.

Designers who can also code will have the options to implement their designs for an additional fee.

Good luck!
Updates

There has been a mistake made in regard to the prize. Pixel Harbor should have it fixed soon.

1st place = £350
2nd place = £250
3rd Place = £150

Thanks,
Dorian
25/11/2011

UPDATE:

1st place will win £350
2nd place will win £250
3rd place will win £150

Everything else is as to the specification.

Thanks
Dorian

Target Market(s)

Builders, Electricians, Plumbers, Tradesman, Small construction companies

Industry/Entity Type

Business

Requirements
Must have
• Totally new designs based around the elements we want to show on each page.

We are looking for something different to the design we already have. But you can use that as a starting point.

Use the included files to see what is required for each page. Here is a brief outline:

Homepage - Testimonials, News, Business Description, Latest Projects and Call to action

About-Us - Team Summary, About the Business and a call to action

Projects Page - Project Details (Oage Title and description), Each project needs a title, content and 2 images.

Testimonials Page - The testifiers name and their comment

Contacts Page - Trovix Map, Company address, business hours, contact form and a call to action.

Please submit final designs in Photoshop or Fireworks format.

Each page has a set of elements. These element must feature in the design of that page. See supporting documents for page details.

All elements must be included in your design. Please do not add any extra element.

Professional look and feel
Nice to have
• Design variations:
Full width designs
Boxed Designs
With AND without carousels
OR static images
Good use of stock images.

Creative use of the elements, dont be restricted/influenced by the default design we have already

Designs based on the 960 grid

```html
<!DOCTYPE html>
<html lang="en">
<head>
<meta charset="utf-8">
<title>kVesta – KR Builders</title>
<link rel="stylesheet" href="https://fonts.googleapis.com/css2?family=Ubuntu:wght@400;500&family=Arimo:wght@400;700&display=swap">
<style>
:root{
  --ink:#1b1b1b;
  --brand:#0d4f7a;
  --brand-light:#1d87c4;
  --sky-top:#8fd7f8;
  --sky-bottom:#22a0e4;
  --btn-top:#6fd0fb;
  --btn-bottom:#27a6e6;
  --btn-dark:#0d5f8e;
  --orange-top:#ffd26a;
  --orange-bottom:#f79a0e;
  --grey-line:#c9c9c9;
  --text:#333;
  --black:#111;
}
*{margin:0;padding:0;box-sizing:border-box}
html,body{width:844px;height:1200px;overflow:hidden;background:#fff}
body{position:relative;font-family:"Arimo",Arial,sans-serif;color:var(--text)}
h1,h2,h3{font-weight:400}
.abs{position:absolute}
.topbar{left:0;top:0;width:844px;height:12px;background:var(--black)}
.header{left:0;top:12px;width:844px;height:93px;background:linear-gradient(#fff 0,#fff 75%,#e6e6e6 100%)}
.logo{left:40px;top:34px;font-family:"Ubuntu",sans-serif;font-weight:500;font-size:33px;letter-spacing:.5px;color:var(--brand)}
.phone-icon{left:512px;top:40px;width:34px;height:32px;border-radius:6px;background:linear-gradient(var(--btn-top),#0f79b7)}
.phone{left:557px;top:43px;font-family:"Ubuntu",sans-serif;font-size:21px;color:#1a7ab0;letter-spacing:.3px}
.tweet{left:714px;top:0;width:81px;height:26px;background:var(--black);border-radius:0 0 14px 14px;color:#ddd;font-size:11px;font-style:italic;text-align:center;line-height:26px}
.tweet svg{position:absolute;left:56px;top:22px}
.hero-photo{left:0;top:105px;width:573px;height:331px;background:linear-gradient(135deg,#9fb2c2 0%,#c9c0ad 40%,#8a7d6c 70%,#b9b2a4 100%)}
.hero-panel{left:573px;top:105px;width:271px;height:331px;background:linear-gradient(var(--sky-top),var(--sky-bottom))}
.hero-title{left:606px;top:159px;font-family:"Ubuntu",sans-serif;font-weight:500;font-size:18.5px;color:#142838;white-space:nowrap}
.hero-text{left:618px;top:204px;width:190px;font-family:"Ubuntu",sans-serif;font-size:15px;line-height:25.5px;color:#fff}
.more{left:670px;top:322px;width:81px;height:27px;border-radius:14px;background:linear-gradient(var(--orange-top),var(--orange-bottom));color:#fff;font-weight:700;font-size:17px;text-align:center;line-height:27px}
.dots{left:692px;top:391px}
.nav-band{left:0;top:436px;width:844px;height:40px;background:linear-gradient(#fafafa,#dcdcdc)}
.nav a{position:absolute;top:442px;height:28px;border-radius:3px;background:linear-gradient(var(--btn-top),var(--btn-bottom));color:#123;font-family:"Ubuntu",sans-serif;font-size:12px;letter-spacing:-.3px;text-align:center;line-height:28px;text-decoration:none}
.nav a.current{background:linear-gradient(#1a79ab,var(--btn-dark));color:#fff}
.card{border-radius:10px}
.testimonials{left:13px;top:493px;width:203px;height:239px;background:linear-gradient(#c4ebfb,#2aa4e4)}
.panel-head{height:31px;width:193px;left:18px;border-radius:8px 8px 0 0;font-family:"Ubuntu",sans-serif;font-size:16px;color:#111;text-align:center;line-height:31px}
.testimonial-head{top:499px;background:linear-gradient(#7fd2f7,#2aa4e4)}
.news-head{top:753px;background:linear-gradient(#f6f6f6,#c8c8c8)}
.avatar{width:62px;height:56px;border:2px solid #fff;background:linear-gradient(#6d7f8e,#3a4652)}
.quote{left:97px;width:114px;font-size:10px;line-height:15px;color:#10202c;padding-left:10px}
.quote b{font-size:15px;line-height:0}
.quote .open{margin-left:-10px;margin-right:1px}
.author{left:101px;font-size:10px;font-weight:700;color:#10202c}
.view-more{font-size:10px}
.news{left:13px;top:747px;width:203px;height:222px;background:linear-gradient(#f3f3f3,#dedede)}
.date{left:22px;width:50px;height:50px;background:linear-gradient(#3caee8,#0f72ad);color:#0b2233;font-size:11px;line-height:15px;text-align:center;padding-top:11px;box-shadow:3px 0 4px rgba(0,0,0,.25)}
.news-text{left:85px;width:110px;font-size:10px;line-height:15px;color:#222}
.section-title{font-family:"Ubuntu",sans-serif;font-size:20px;color:var(--brand);white-space:nowrap}
.rule{height:1px;background:linear-gradient(90deg,rgba(29,135,196,0),#7cc2e8)}
.rule::after{content:"";position:absolute;right:-6px;top:-6px;width:13px;height:13px;border-radius:50%;background:radial-gradient(circle at 40% 35%,#9be0ff,#1d8fd0)}
.copy{left:262px;width:538px;font-size:10.3px;line-height:17.7px;color:#222}
.carousel{left:268px;top:772px;width:551px;height:173px;border:1px solid #9a9a9a;border-radius:4px;background:#fff}
.rail{top:777px;width:26px;height:164px;background:linear-gradient(90deg,#f4f4f4,#dedede);border-radius:3px}
.arrow{width:13px;height:13px;border-radius:50%;background:#3aa9e6}
.thumb{top:789px;width:154px;height:117px;border-radius:3px}
.caption{top:910px;width:150px;font-size:9.6px;line-height:16px;color:#111;text-align:center}
.footer{left:0;top:985px;width:844px;height:138px;background:linear-gradient(#ececec,#f6f6f6 50%,#e8e8e8)}
.divider{top:993px;width:1px;height:122px;background:var(--grey-line)}
.foot-title{top:1001px;font-family:"Ubuntu",sans-serif;font-size:17px;color:#111}
.social{top:1062px;width:27px;height:27px;border-radius:5px;background:linear-gradient(#7cc7ee,#1e6fa8)}
.email-field{left:345px;top:1030px;width:168px;height:25px;border:1px solid #aaa;background:#fff}
.subscribe{left:344px;top:1066px;width:117px;height:29px;border-radius:4px;background:linear-gradient(#6d6d6d,#2e2e2e);color:#fff;font-size:13px;text-align:center;line-height:29px}
.contact-text{font-size:10.5px;line-height:16px;color:#111}
.bottombar{left:0;top:1129px;width:844px;height:6px;background:var(--black)}
.legal{left:263px;top:1155px;font-size:10.5px;color:#222;white-space:nowrap}
.legal span{margin:0 13px}
.copyright{left:291px;top:1181px;font-size:10.5px;color:#222;white-space:nowrap}
</style>
</head>
<body>
<div class="abs topbar"></div>
<header class="abs header"></header>
<div class="abs logo">kVesta</div>
<div class="abs phone-icon">
  <svg width="34" height="32" viewBox="0 0 34 32"><path d="M11 8c2-1 3 0 4 3s-1 3-1 4c1 2 3 4 5 5 1 0 1-2 4-1s4 2 3 4c-1 2-3 3-5 2-5-2-9-6-11-11-1-2 0-5 1-6z" fill="#fff"/></svg>
</div>
<div class="abs phone">444 210 987</div>
<div class="abs tweet">Tweet Us<svg width="12" height="12"><path d="M0 0h12L10 12z" fill="#111"/></svg></div>

<div class="abs hero-photo" role="img" aria-label="Two site managers in hard hats reviewing plans at a construction site"></div>
<section class="abs hero-panel"></section>
<h2 class="abs hero-title">Lorem ipsum dolor amet</h2>
<p class="abs hero-text">Lorem ipsum dolor sit amet, consectetuer adipiscing elit. Lorem ipsum dolor sit amet, adipiscing&nbsp; elit</p>
<div class="abs more">More</div>
<svg class="abs dots" width="58" height="18"><circle cx="9" cy="9" r="8.5" fill="#f7e46a"/><circle cx="29" cy="9" r="8.5" fill="#fff"/><circle cx="49" cy="9" r="8.5" fill="#fff"/></svg>

<div class="abs nav-band"></div>
<nav class="nav">
  <a class="current" style="left:25px;width:81px">HOME</a>
  <a style="left:119px;width:81px">ABOUT US</a>
  <a style="left:212px;width:89px">TESTIMONIALS</a>
  <a style="left:314px;width:82px">PORTFOLIO</a>
  <a style="left:408px;width:81px">CONTACTS</a>
</nav>

<aside class="abs card testimonials"></aside>
<div class="abs panel-head testimonial-head">TESTIMONIAL</div>
<div class="abs avatar" style="left:30px;top:542px" role="img" aria-label="Portrait of the client"></div>
<p class="abs quote" style="top:541px"><b class="open">“</b>Lorem ipsum dolor sit amet, consectetuer adipiscing elit.<b>”</b></p>
<div class="abs author" style="top:592px">Mr.Halvorsen</div>
<div class="abs avatar" style="left:30px;top:628px" role="img" aria-label="Portrait of the client"></div>
<p class="abs quote" style="top:631px"><b class="open">“</b>Lorem ipsum dolor sit amet, consectetuer adipiscing elit. <b>”</b></p>
<div class="abs author" style="top:682px">Mr.Halvorsen</div>
<div class="abs view-more" style="left:104px;top:709px;color:#fff">View more</div>

<aside class="abs card news"></aside>
<div class="abs panel-head news-head">LATEST NEWS</div>
<div class="abs date" style="top:804px">Dec 3,<br>2011</div>
<p class="abs news-text" style="top:805px">Lorem ipsum dolor sit amet, consectetuer adipiscing elit.</p>
<div class="abs date" style="top:881px">Dec 3,<br>2011</div>
<p class="abs news-text" style="top:879px">Lorem ipsum dolor sit amet, consectetuer adipiscing elit.</p>
<div class="abs view-more" style="left:91px;top:944px;color:#c0151b">View more</div>

<h1 class="abs section-title" style="left:255px;top:500px">WELCOME TO KR BUILDERS</h1>
<div class="abs rule" style="left:258px;top:529px;width:255px"></div>
<p class="abs copy" style="top:541px">Lorem ipsum dolor sit amet, consectetuer adipiscing elit. Nam nibh. Nunc varius facilisis eros. Sed erat. Lorem ipsum dolor sit amet, consectetuer adipiscing elit. Nam nibh. Nunc varius facilisis eros. Sed erat. Lorem ipsum dolor sit amet, consectetuer adipiscing elit. Nam nibh. Nunc varius facilisis eros. Sed erat. Lorem ipsum dolor sit amet, consectetuer adipiscing elit. Nam nibh. Nunc varius facilisis eros. Sed erat.</p>
<p class="abs copy" style="top:629px">Lorem ipsum dolor sit amet, consectetuer adipiscing elit. Nam nibh. Nunc varius facilisis eros. Sed erat. Lorem ipsum dolor sit amet, consectetuer adipiscing elit. Nam nibh. Nunc varius facilisis eros. Sed erat. Lorem ipsum dolor sit amet, consectetuer adipiscing elit. Nam nibh. Nunc varius facilisis eros. Sed erat. Lorem ipsum dolor sit amet, consectetuer adipiscing elit. Nam nibh. Nunc varius facilisis eros. Sed erat.</p>

<h2 class="abs section-title" style="left:262px;top:718px">Latest Projects</h2>
<div class="abs rule" style="left:262px;top:752px;width:157px"></div>
<div class="abs carousel"></div>
<div class="abs rail" style="left:276px"></div>
<div class="abs rail" style="left:785px"></div>
<div class="abs arrow" style="left:279px;top:849px"></div>
<div class="abs arrow" style="left:794px;top:849px"></div>
<div class="abs thumb" style="left:308px;background:linear-gradient(135deg,#9fc4e6,#4f6f8e 60%,#c9d3dc)" role="img" aria-label="Glass office building against the sky"></div>
<div class="abs thumb" style="left:467px;background:linear-gradient(160deg,#7fa6d4,#c9c4b8 55%,#8b8478)" role="img" aria-label="Concrete office block with bare trees"></div>
<div class="abs thumb" style="left:626px;background:linear-gradient(150deg,#8fb5e0,#55606c 55%,#a9b2bb)" role="img" aria-label="High-rise towers joined by a sky bridge"></div>
<p class="abs caption" style="left:304px">Lorem ipsum dolor sit amet, consectetuer adipiscing elit.</p>
<p class="abs caption" style="left:464px">Lorem ipsum dolor sit amet, consectetuer adipiscing elit.</p>
<p class="abs caption" style="left:625px">Lorem ipsum dolor sit amet, consectetuer adipiscing elit.</p>

<footer class="abs footer"></footer>
<div class="abs divider" style="left:268px"></div>
<div class="abs divider" style="left:589px"></div>
<h3 class="abs foot-title" style="left:64px">Follow Us</h3>
<div class="abs social" style="left:38px"></div>
<div class="abs social" style="left:71px"></div>
<div class="abs social" style="left:104px"></div>
<div class="abs social" style="left:139px;background:linear-gradient(#fdfdfd,#d6d6d6)"></div>
<div class="abs social" style="left:175px;background:linear-gradient(#ffb347,#ef7b10)"></div>
<h3 class="abs foot-title" style="left:343px">Newsletter</h3>
<div class="abs email-field"></div>
<div class="abs subscribe">Subscribe</div>
<h3 class="abs foot-title" style="left:614px">Contact</h3>
<p class="abs contact-text" style="left:655px;top:1034px">Lorem ipsum dolor sit amet,<br>consectetuer adipiscing elit.</p>
<p class="abs contact-text" style="left:634px;top:1072px">Phone : 023 555 0142<br>Email: info@krbuilders.com</p>

<div class="abs bottombar"></div>
<p class="abs legal">Privacy Policy<span>|</span>Terms &amp; Conditions<span>|</span>Contact Us</p>
<p class="abs copyright">Copyright © kVesta, All Rights Reserved</p>
</body>
</html>
```